Eye Institute Needs New Look

I have very detailed notes to guide you but be creative where needed. Attached are a screenshot of a wp theme i like and how i would like most content cut out and certain parts used. Site should be in blues.

Their current site is CLEARVALEOPTIC.com and you can pull some content and their logo from there (sorry, that is the best i can get from them for logo)

the theme I like is: http://brintor-sample.com/velmora_wp/

but review attached notes to see changes I want and direction of website.

All of the designs are VERY well done and followed instructions well.  They all are very similar and what I was looking for.  But all designers made two consistent mistakes.  For any that wish to be considered and still in the running for the final decision, I need these two changes to your submissions:

1) the designs are too clean / white.  I was looking for the content areas to be shades of blue , dark blue, etc so that the new site design isn't white and clean like their current site.

2) the boxes under the header.  I have seen versions with the grays and blues.  Can we try it with some bold multi colors for pop like red, yellow, green, orange, etc?

3) overall, this is an example site they liked http://www.mypeltonvision.com/ , can you get the site to have some splash of a bold complimentary highlight color and less overall white in the site?

Thank you and I look forward to submissions.  I need to show the client tomorrow so hopefully anyone still considering can get me revisions in the next 12 hours.

```html
<!DOCTYPE html>
<html lang="en">
<head>
<meta charset="utf-8">
<title>Clearvale Optic Institute</title>
<link href="https://fonts.googleapis.com/css2?family=Ubuntu:wght@300;400;500;700&family=Roboto:wght@300;400&display=swap" rel="stylesheet">
<style>
:root{
  --ink:#ffffff;
  --bar:#0b0d12;
  --brand:#1aa0d8;
  --navy:#262d45;
  --band:#08508b;
  --sky:#6fb4e8;
  --foot:#333333;
  --foot-dark:#2a2a2a;
  --map:#0b78c9;
}
*{margin:0;padding:0;box-sizing:border-box}
html,body{width:885px;height:1200px;overflow:hidden;background:var(--navy)}
body{position:relative;font-family:'Roboto',Arial,sans-serif;color:var(--ink)}
.abs{position:absolute}

/* hero */
.hero{left:0;top:0;width:885px;height:400px;background:linear-gradient(120deg,#3f6b2c 0%,#7a9a54 25%,#c9b69a 45%,#8a5a3a 65%,#4a2e20 85%,#3d6a2a 100%)}
.topbar{left:0;top:0;width:885px;height:66px;background:rgba(8,10,14,.82)}
.logo{left:120px;top:18px;display:flex;align-items:center;gap:8px;font-family:'Ubuntu',sans-serif;font-weight:700;font-size:21px;color:var(--brand)}
.logo .dot{width:14px;height:14px;border-radius:50%;background:var(--brand)}
.contact-line{left:660px;top:8px;display:flex;align-items:center;gap:6px;font-family:'Ubuntu',sans-serif;font-weight:500;font-size:14px;color:var(--brand)}
.nav{left:0;top:0;height:66px}
.nav a{position:absolute;top:47px;font-family:'Ubuntu',sans-serif;font-weight:500;font-size:11px;color:var(--brand);text-decoration:none;white-space:nowrap}
.nav .home{left:298px;top:0;width:50px;height:66px;background:linear-gradient(#0a3e70,#1a7cc4);color:#fff;text-align:center;padding-top:47px}
.caption{left:0;top:266px;width:355px;height:111px;background:rgba(25,22,22,.78);padding:6px 0 0 68px}
.caption h1{font-family:'Ubuntu',sans-serif;font-weight:700;font-size:29px;letter-spacing:.3px}
.caption p{font-family:'Ubuntu',sans-serif;font-weight:300;font-size:14px;line-height:20px;margin-top:2px}
.caption-bar{left:362px;top:266px;width:25px;height:111px;background:var(--band)}

/* band */
.band{left:0;top:400px;width:885px;height:30px;background:var(--band)}
.dots{left:416px;top:411px;display:flex;gap:7px}
.dots i{width:8px;height:8px;border-radius:50%;background:#fff}
.dots i:first-child{background:#111}
.notch{left:432px;top:429px}

/* service boxes */
.services{left:0;top:430px;width:885px;height:226px;background:var(--navy)}
.card{top:452px;width:177px;height:173px;text-align:center;box-shadow:3px 4px 8px rgba(0,0,0,.45);overflow:hidden}
.card h2{font-family:'Ubuntu',sans-serif;font-weight:700;font-size:17px;margin-top:13px}
.card svg.icon{margin-top:6px}
.card p{font-weight:400;font-size:9.5px;line-height:11.5px;padding:0 18px;margin-top:8px}
.card .more{position:absolute;left:0;right:0;bottom:10px;font-family:'Ubuntu',sans-serif;font-weight:700;font-size:9.5px}
.card .fold{position:absolute;left:0;top:0}
.c-red{left:66px;background:linear-gradient(#e01616,#b70b0b)}
.c-yellow{left:256px;background:linear-gradient(#f6cb1a,#e2a80b)}
.c-green{left:445px;background:linear-gradient(#86cc30,#67ad25)}
.c-orange{left:635px;background:linear-gradient(#fa9f12,#ef8408)}

/* feature */
.feature{left:0;top:656px;width:885px;height:230px;background:linear-gradient(#0c5391,#0a4478);border-top:1px solid #2a74b8}
.feature-col h3{font-family:'Ubuntu',sans-serif;font-weight:300;font-size:19px;line-height:24px;color:#fff}
.feature-col p,.feature-col li{font-weight:300;font-size:9.6px;line-height:14.5px;color:var(--sky);letter-spacing:.2px}
.col-left{left:67px;top:668px;width:345px}
.col-left p{margin-top:3px}
.col-left p+p{margin-top:30px}
.divider{left:442px;top:672px;width:2px;height:210px;background:linear-gradient(#1a6ab0,#3f93d8,#1a6ab0)}
.col-right{left:465px;top:668px;width:355px}
.col-right p{margin-top:3px}
.col-right ul{list-style:none;margin-top:7px}
.col-right li{position:relative;padding-left:13px;margin-bottom:8px}
.col-right li::before{content:"";position:absolute;left:2px;top:5px;width:4px;height:4px;border-radius:50%;background:var(--sky)}

/* footer */
.foot-head{left:0;top:886px;width:885px;height:32px;background:linear-gradient(#555,#444);border-top:1px solid #777}
.foot-head h4{position:absolute;top:9px;font-family:'Ubuntu',sans-serif;font-weight:500;font-size:12.5px;letter-spacing:.3px}
.foot-body{left:0;top:918px;width:885px;height:186px;background:var(--foot)}
.testimonial{left:74px;top:918px;width:192px;height:186px;background:#3a3a3a;padding:12px 20px 0 15px;font-weight:300;font-size:10.3px;line-height:15.3px;color:#e6e6e6}
.testimonial .by{margin-top:15px}
.links{list-style:none;font-weight:300;font-size:10.3px;color:#e6e6e6}
.links li{position:relative;padding-left:15px}
.links li::before{content:"";position:absolute;left:2px;top:6px;width:4px;height:4px;border-radius:50%;background:#111}
.nav-links{left:286px;top:930px}
.nav-links li{height:28.3px}
.map-box{left:443px;top:918px;width:194px;height:178px;background:#383838;box-shadow:2px 2px 6px rgba(0,0,0,.4)}
.map{left:457px;top:932px;width:150px;height:145px;background:linear-gradient(160deg,#0d86d8,var(--map));border-radius:40% 20% 30% 50%}
.map-note{left:450px;top:1081px;font-weight:300;font-size:9.6px;color:#e6e6e6}
.contact-links{left:654px;top:930px}
.contact-links li{height:28.3px}
.legal{left:0;top:1104px;width:885px;height:96px;background:var(--foot-dark);border-top:1px solid #555;text-align:center;font-weight:300;font-size:9.6px;line-height:14px;color:#e0e0e0;padding:5px 105px 0}
.legal .copy{margin-top:13px}
.to-top{left:797px;top:1122px;width:12px;height:12px;border-radius:50%;background:#555}
</style>
</head>
<body>

<div class="abs hero" role="img" aria-label="Photo of friends jumping happily into a resort pool"></div>
<div class="abs topbar"></div>
<div class="abs logo"><span class="dot"></span>Clearvale Optic</div>
<div class="abs contact-line">
  <svg width="14" height="14" viewBox="0 0 14 14"><circle cx="7" cy="7" r="6" fill="none" stroke="#1aa0d8" stroke-width="1.3"/><path d="M4.6 4.2l1.2-.3.7 1.6-.8.6c.4.9 1 1.5 1.9 1.9l.6-.8 1.6.7-.3 1.2c-2.7.2-5.1-2.2-4.9-4.9z" fill="#1aa0d8"/></svg>
  (555) 318-2046
</div>
<nav class="abs nav">
  <a class="home" href="#">HOME</a>
  <a href="#" style="left:371px">Our Practice</a>
  <a href="#" style="left:483px">Services</a>
  <a href="#" style="left:567px">Education</a>
  <a href="#" style="left:662px">Locations</a>
  <a href="#" style="left:757px">Contact</a>
</nav>

<div class="abs caption">
  <h1>LASIK SURGERY</h1>
  <p>TRUSTED<br>Why are people trusting Clearvale Optic<br>Institute for their eyecare?</p>
</div>
<div class="abs caption-bar"></div>

<div class="abs band"></div>
<div class="abs dots"><i></i><i></i><i></i><i></i></div>
<svg class="abs notch" width="22" height="11" viewBox="0 0 22 11"><path d="M0 0h22L11 11z" fill="#08508b"/></svg>

<div class="abs services"></div>

<section class="abs card c-red">
  <svg class="fold" width="40" height="80"><path d="M0 0h4l36 40L0 80z" fill="#8a0606"/></svg>
  <h2>Cataracts</h2>
  <svg class="icon" width="50" height="32" viewBox="0 0 50 32"><path d="M2 16C12 2 38 2 48 16 38 30 12 30 2 16z" fill="none" stroke="#fff" stroke-width="4"/><circle cx="25" cy="16" r="8" fill="#fff"/><circle cx="25" cy="16" r="3.5" fill="#d11"/></svg>
  <p>Lorem ipsum dolor sit amet, consectetuer adipiscing elit, sed diam nonummy nibh euismod tincidunt Lorem ipsum</p>
  <div class="more">read more +</div>
</section>

<section class="abs card c-yellow">
  <svg class="fold" width="40" height="80"><path d="M0 0h4l36 40L0 80z" fill="#b9870a"/></svg>
  <h2>Laser</h2>
  <svg class="icon" width="50" height="32" viewBox="0 0 50 32"><g stroke="#fff" stroke-width="1.4"><path d="M17 2v28M3 16h28M7 6l20 20M27 6L7 26M11 3l12 26M23 3L11 29M4 10l26 12M30 10L4 22"/><path d="M17 16h32" stroke-width="2"/></g><circle cx="17" cy="16" r="5" fill="#fff"/></svg>
  <p>Lorem ipsum dolor sit amet, consectetuer adipiscing elit, sed diam nonummy nibh euismod tincidunt Lorem ipsum</p>
  <div class="more">read more +</div>
</section>

<section class="abs card c-green">
  <svg class="fold" width="40" height="80"><path d="M0 0h4l36 40L0 80z" fill="#4f8a1c"/></svg>
  <h2>Glaucoma</h2>
  <svg class="icon" width="50" height="32" viewBox="0 0 50 32"><path d="M2 16C12 2 38 2 48 16 38 30 12 30 2 16z" fill="#fff"/><circle cx="25" cy="16" r="8" fill="#74bb2b"/><circle cx="25" cy="16" r="4" fill="#fff"/></svg>
  <p>Lorem ipsum dolor sit amet, consectetuer adipiscing elit, sed diam nonummy nibh euismod tincidunt Lorem ipsum</p>
  <div class="more">read more +</div>
</section>

<section class="abs card c-orange">
  <svg class="fold" width="40" height="80"><path d="M0 0h4l36 40L0 80z" fill="#b85d05"/></svg>
  <h2>Eye shop</h2>
  <svg class="icon" width="50" height="32" viewBox="0 0 50 32"><circle cx="30" cy="12" r="10" fill="none" stroke="#fff" stroke-width="3"/><path d="M24 12c3-4 9-4 12 0-3 4-9 4-12 0z" fill="#fff"/><path d="M22 19l-8 10" stroke="#fff" stroke-width="5" stroke-linecap="round"/></svg>
  <p>Lorem ipsum dolor sit amet, consectetuer adipiscing elit, sed diam nonummy nibh euismod tincidunt Lorem ipsum</p>
  <div class="more">read more +</div>
</section>

<div class="abs feature"></div>
<article class="abs feature-col col-left">
  <h3>Presenting the LUMA System</h3>
  <p>LUMA, Clarwave® Refractive Analysis, is a revolutionary diagnostic device with Clarwave technology that is designed to take intraoperative wavefront aberrometry to a higher level of performance.</p>
  <p>The Clarwave technology has a precise light source and optics, the assurance of a live display of the eye, a convenient system-aligned, on-demand reticle and optimized algorithms to guide every refractive decision you make for your cataract patients.</p>
</article>
<div class="abs divider"></div>
<article class="abs feature-col col-right">
  <h3>Optimized. On-Demand. Performance.</h3>
  <p>With the LUMA System®, Brightec® is revolutionizing the way you think about intraoperative wavefront analysis.</p>
  <ul>
    <li>Clarwave® technology optimizes intraoperative wavefront data to calculate IOL power and guide standard, premium or toric IOL selection</li>
    <li>LUMA System® enables opportunity for better cataract outcomes and higher patient satisfaction</li>
    <li>Use of the LUMA System reduces potential for costly retreatments due to postoperative surprises</li>
    <li>Revised, affordable pricing model and practice support assistance making Brightec a true partner in and out of the OR</li>
  </ul>
</article>

<div class="abs foot-head">
  <h4 style="left:90px">TESTIMONIALS</h4>
  <h4 style="left:309px">NAVIGATION</h4>
  <h4 style="left:501px">LOCATIONS</h4>
  <h4 style="left:679px">CONTACT US</h4>
</div>
<div class="abs foot-body"></div>
<blockquote class="abs testimonial">
  <p>After my cataract surgery... it was absolutely phenominal. My eyesight was restored back to normal. It's been nine years (since my cataract surgery), and I haven't worn glasses ever since. It was so comfortable, there was no pain involved.</p>
  <p class="by">— Dana R., Sterling Heights, Michigan</p>
</blockquote>
<ul class="abs links nav-links">
  <li>Home</li><li>Appointment Request</li><li>Our Practice</li><li>Resources</li><li>Locations</li><li>Contact</li>
</ul>
<div class="abs map-box"></div>
<div class="abs map" role="img" aria-label="Map of Michigan showing the practice region"></div>
<div class="abs map-note">Visit us at any of our convenient locations!</div>
<ul class="abs links contact-links">
  <li>Schedule an appointment</li><li>Go to our contact page</li>
</ul>

<footer class="abs legal">
  <p>Clearvale Optic Institute offers patient a variety of Ophthalmology, Refractive &amp; Cosmetic Services including, LASIK surgery, Eye Exams, Glaucoma Diagnosis &amp; Treatment, Cataract Surgery, Interocular Lens Placement (IOL's), Treatment for Diabetic Retinopathy, Retinal Surgery, Treatment for Macular Degeration, Corneal Transplants, Relaxa, Thermalift, Contourline Cellulite Treatment, Dermafill &amp; Eye Lid Surgery. Serving patients in the Detroit Michigan area including, Sterling Heights &amp; Chesterfield Township.</p>
  <p class="copy">Copyright © 2013 Clearvale Optic Institute. All rights reserved.</p>
</footer>
<div class="abs to-top"></div>

</body>
</html>
```